Logo design and Businesscard and letterhead for Technology Company

We need logo design for a new company based in Atlanta called "Vornimel". We provide information about technology Product and service provider companies, information about their Products and services. Our initial focus is to List various companies and their products, various consulting companies and their services. We want to convey the message that this will be one stop shop to find out all the information to make smart technology decisions

I am looking for Logo, Business Card and Letterhead.

Target Market(s)

Companies that have IT department, IT users such as Developers, Managers, C level, Technology Product companies , Consulting companies and service providers.

Industry/Entity Type

It Company

Requirements
Must have
• Looking for some Unique design idea.
Nice to have
• I want something that connects information across technologies between technology buyers and sellers.
Should not have
• No puzzle design.

```html
<!DOCTYPE html>
<html lang="en">
<head>
<meta charset="utf-8">
<title>Vornimel – Letterhead and Business Cards</title>
<link rel="stylesheet" href="https://fonts.googleapis.com/css2?family=Oswald:wght@300;400;500&display=swap">
<style>
  :root {
    --paper: #ffffff;
    --outside: #ffffff;
    --trim: #d6d6d6;
    --orange: #f7870f;
    --green: #6db33f;
    --green-faint: #dcebd0;
    --black: #000000;
    --card-light: #e9ecee;
    --grey-text: #8a8a8a;
    --dark-text: #555555;
  }
  * { margin: 0; padding: 0; box-sizing: border-box; }
  html, body { width: 878px; height: 1200px; overflow: hidden; background: var(--outside); }
  body { position: relative; font-family: "Oswald", "Arial Narrow", sans-serif; }

  .crop-marks { position: absolute; inset: 0; width: 878px; height: 1200px; }

  .letterhead {
    position: absolute; left: 44px; top: 40px; width: 791px; height: 1116px;
    background: var(--paper); border: 1px solid var(--trim); overflow: hidden;
  }
  .letterhead__accent {
    position: absolute; left: -40px; top: -30px; width: 200px; height: 200px;
    border: 22px solid var(--green-faint); border-radius: 50%;
  }

  .brand { display: flex; align-items: center; color: var(--orange); font-weight: 300; line-height: 1; }
  .brand__dot { border-radius: 50%; background: var(--green); flex: none; }

  .brand--header { position: absolute; right: 28px; top: 88px; font-size: 36px; letter-spacing: 2px; gap: 10px; }
  .brand--header .brand__dot { width: 16px; height: 16px; }

  .brand--feature { position: absolute; left: 416px; top: 520px; font-size: 68px; letter-spacing: 4px; gap: 16px; }
  .brand--feature .brand__dot { width: 28px; height: 28px; }

  .card {
    position: absolute; top: 649px; width: 328px; height: 200px; border-radius: 10px; overflow: hidden;
  }
  .card--front { left: 55px; background: var(--black); }
  .card--front .brand { position: absolute; left: 0; right: 0; top: 124px; justify-content: center; font-size: 28px; letter-spacing: 2px; gap: 10px; }
  .card--front .brand__dot { width: 14px; height: 14px; }

  .card--back { left: 415px; background: linear-gradient(180deg, #f0f2f3, var(--card-light)); }
  .card--back .brand { position: absolute; left: 24px; top: 20px; font-size: 20px; letter-spacing: 1px; gap: 7px; }
  .card--back .brand__dot { width: 12px; height: 12px; }
  .card__accent { position: absolute; left: -20px; top: 18px; width: 120px; height: 120px; border: 14px solid var(--green-faint); border-radius: 50%; opacity: .7; }
  .card__owner { position: absolute; left: 28px; top: 80px; font-size: 10px; color: var(--dark-text); font-weight: 500; }
  .card__owner .sep { color: var(--orange); padding: 0 3px; }
  .card__owner .role { color: var(--grey-text); font-weight: 400; }
  .card__contact { position: absolute; left: 206px; top: 71px; font-size: 9px; line-height: 15px; color: var(--grey-text); list-style: none; }
  .card__contact b { color: var(--dark-text); font-weight: 500; }
  .card__wave { position: absolute; left: 0; bottom: 0; width: 328px; height: 84px; }

  .footer { position: absolute; left: 0; bottom: 0; width: 791px; height: 92px; }
  .footer__wave { position: absolute; inset: 0; width: 791px; height: 92px; }
  .footer__contact {
    position: absolute; left: 0; right: 0; bottom: 22px; display: flex; justify-content: center;
    list-style: none; font-size: 12px; letter-spacing: .8px; color: #ffffff;
  }
  .footer__contact li + li::before { content: "|"; color: var(--orange); padding: 0 8px; }
  .footer__contact .label { color: var(--orange); }
</style>
</head>
<body>

<svg class="crop-marks" viewBox="0 0 878 1200" aria-hidden="true">
  <g stroke="#bdbdbd" stroke-width="1">
    <line x1="44" y1="0" x2="44" y2="28"/><line x1="0" y1="40" x2="32" y2="40"/>
    <line x1="835" y1="0" x2="835" y2="28"/><line x1="846" y1="40" x2="878" y2="40"/>
    <line x1="44" y1="1168" x2="44" y2="1200"/><line x1="0" y1="1156" x2="32" y2="1156"/>
    <line x1="835" y1="1168" x2="835" y2="1200"/><line x1="846" y1="1156" x2="878" y2="1156"/>
  </g>
</svg>

<main class="letterhead">
  <div class="letterhead__accent"></div>

  <div class="brand brand--header"><span class="brand__dot"></span><span>vornimel</span></div>

  <div class="brand brand--feature"><span class="brand__dot"></span><span>vornimel</span></div>

  <section class="card card--front">
    <div class="brand"><span class="brand__dot"></span><span>vornimel</span></div>
  </section>

  <section class="card card--back">
    <div class="card__accent"></div>
    <div class="brand"><span class="brand__dot"></span><span>vornimel</span></div>
    <p class="card__owner">Name of the Owner<span class="sep">|</span><span class="role">Designation</span></p>
    <ul class="card__contact">
      <li><b>Tel:</b> 00 482 61937</li>
      <li><b>Fax:</b> 00 482 61938</li>
      <li><b>E-mail:</b> hello@vornimel.net</li>
    </ul>
    <svg class="card__wave" viewBox="0 0 328 84" preserveAspectRatio="none" aria-hidden="true">
      <path d="M0 22 C70 -4 150 10 210 22 C260 32 300 20 328 8 L328 84 L0 84 Z" fill="var(--orange)"/>
      <path d="M0 34 C70 8 150 18 210 30 C260 40 300 30 328 16 L328 84 L0 84 Z" fill="var(--black)"/>
    </svg>
  </section>

  <footer class="footer">
    <svg class="footer__wave" viewBox="0 0 791 92" preserveAspectRatio="none" aria-hidden="true">
      <path d="M0 26 C160 10 330 32 520 30 C640 28 730 14 791 0 L791 92 L0 92 Z" fill="var(--orange)"/>
      <path d="M0 34 C160 18 330 38 520 36 C640 34 730 22 791 10 L791 92 L0 92 Z" fill="var(--black)"/>
    </svg>
    <ul class="footer__contact">
      <li><span class="label">Tel:</span> 00 482 61937</li>
      <li><span class="label">Fax:</span> 00 482 61938</li>
      <li><span class="label">E-mail :</span> hello@vornimel.net</li>
      <li><span class="label">Website :</span> www.vornimel.net</li>
      <li><span class="label">Location :</span> Brenford, USA.</li>
    </ul>
  </footer>
</main>

</body>
</html>
```